Kitchen Renovation in YOUR area

We need a template for a flyer that we can hand out in neighbourhoods when we're finished renovating a kitchen. Every neighbourhood, we'll swap out a before and after picture to personalize to that neighbourhood. These will be low print run flyers (30-50 each time). We're really hoping that they'll see *their* kitchen in the BEFORE section (since many houses in neighbourhoods are similar) and see what they're kitchen could look like in the AFTER section. So I want the BEFORE and AFTER photos to be easily swapped in and out on my end. I have lots of photos if needed.

Target Market(s)

Home owners looking to have their kitchen's renovated. This is typically in the 35-55 age range. Primarily women.

Colors

Designer to choose colors to be used in the design.

Requirements
Must have
• My logo, a before (0962) and an after (8281) that I can swap out as I go from neighborhood to neighborhood. All the other design elements can be permanent.
• My website address: MaplestoneRemodels.com
Nice to have
• A background of some kitchen work I've done (1171.jpg). I've also included some copy. That copy can change - that's just something I did up quickly. Use what you can and I can make changes later

```html
<!DOCTYPE html>
<html lang="en">
<head>
<meta charset="utf-8">
<title>Maplestone Remodels – Kitchen Refacing Flyer</title>
<link href="https://fonts.googleapis.com/css2?family=Ubuntu:wght@400;500;700&family=Open+Sans:ital,wght@0,400;0,600;0,700;1,600;1,700&display=swap" rel="stylesheet">
<style>
  :root{
    --brand-blue:#1f6aa8;
    --brand-blue-dark:#175a92;
    --slate:#55595e;
    --panel-grey:#6f7275;
    --ink:#3b3e42;
    --paper:#ffffff;
    --canvas:#f1f2f4;
  }
  *{box-sizing:border-box;margin:0;padding:0}
  html,body{width:703px;height:1200px;overflow:hidden;background:var(--canvas)}
  .flyer{
    position:absolute;left:21px;top:131px;width:661px;height:937px;
    background:var(--paper);overflow:hidden;
    box-shadow:8px 14px 30px rgba(0,0,0,.22);
    font-family:"Open Sans",Arial,sans-serif;color:var(--ink);
  }
  .brand-name{
    position:absolute;left:57px;top:52px;
    font-family:"Ubuntu",Arial,sans-serif;font-weight:500;font-size:30px;line-height:1;
    color:var(--slate);display:flex;align-items:center;gap:10px;
  }
  .brand-mark{width:16px;height:16px;border-radius:50%;background:var(--brand-blue)}
  .roof{position:absolute;left:0;top:0;width:661px;height:170px}
  .hero-photo{
    position:absolute;left:28px;top:164px;width:607px;height:305px;
    background:linear-gradient(160deg,#d9dadc 0%,#9ea1a5 38%,#6f7378 55%,#e6e7e9 75%,#cfd1d4 100%);
  }
  .title-block{
    position:absolute;left:0;top:478px;width:391px;height:203px;
    background:var(--brand-blue);color:#fff;padding:30px 0 0 58px;
    font-family:"Ubuntu",Arial,sans-serif;
  }
  .title-main{font-weight:500;font-size:45px;line-height:1;letter-spacing:.5px}
  .title-sub{font-weight:500;font-size:36px;line-height:1.1;margin-top:4px}
  .title-tagline{font-weight:400;font-size:16.5px;line-height:1.22;margin-top:18px}
  .compare-photo{position:absolute;left:404px;width:231px}
  .compare-photo.before{top:483px;height:152px;
    background:linear-gradient(135deg,#b98156 0%,#8d5a36 45%,#3e3a38 70%,#a87048 100%)}
  .compare-photo.after{top:644px;height:159px;
    background:linear-gradient(135deg,#f4f4f3 0%,#e3e3e2 45%,#c9c9c9 65%,#c28a58 100%)}
  .photo-tag{
    position:absolute;right:-6px;top:2px;background:var(--brand-blue);color:#fff;
    font-family:"Open Sans",Arial,sans-serif;font-weight:700;font-size:11px;letter-spacing:.4px;
    padding:1px 10px 1px 14px;clip-path:polygon(8px 0,100% 0,100% 100%,0 100%);
  }
  .contact-panel{
    position:absolute;left:404px;top:812px;width:231px;height:125px;
    background:var(--panel-grey);color:#fff;padding:13px 0 0 20px;
    font-weight:700;font-size:10.5px;
  }
  .contact-item{display:flex;align-items:flex-start;gap:8px;margin-bottom:7px;line-height:1.2}
  .contact-item svg{flex:none;width:11px;height:11px;margin-top:1px}
  .body-copy{position:absolute;left:58px;top:693px;width:312px}
  .lead{color:var(--brand-blue);font-weight:700;font-style:italic;font-size:11.5px;line-height:1.25;margin-bottom:11px}
  .benefit-list{list-style:none}
  .benefit{position:relative;padding-left:16px;font-size:10px;line-height:1.22;text-align:justify;margin-bottom:13px}
  .benefit svg{position:absolute;left:0;top:2px;width:9px;height:9px}
  .highlight{color:var(--brand-blue);font-weight:700}
</style>
</head>
<body>
  <article class="flyer">
    <svg class="roof" viewBox="0 0 661 170" aria-hidden="true">
      <polygon points="483,29 351,141 621,141" fill="var(--brand-blue)"/>
      <rect x="0" y="141" width="621" height="14" fill="var(--brand-blue)"/>
      <rect x="0" y="141" width="17" height="29" fill="var(--brand-blue)"/>
      <g fill="#fff">
        <rect x="461" y="87" width="19" height="17"/>
        <rect x="483" y="87" width="19" height="17"/>
        <rect x="461" y="107" width="19" height="17"/>
        <rect x="483" y="107" width="19" height="17"/>
      </g>
    </svg>
    <svg style="position:absolute;left:0;top:155px" width="17" height="323" aria-hidden="true">
      <rect width="17" height="323" fill="var(--brand-blue)"/>
    </svg>

    <div class="brand-name"><span class="brand-mark"></span>Maplestone Remodels</div>

    <div class="hero-photo" role="img" aria-label="Photo of a finished white kitchen with grey mosaic backsplash, granite counter and stainless range"></div>

    <section class="title-block">
      <h1 class="title-main">MAPLESTONE</h1>
      <p class="title-sub">REMODELS</p>
      <p class="title-tagline">TURN YOUR KITCHEN INTO YOUR<br>DREAM KITCHEN BY REFACING!</p>
    </section>

    <div class="compare-photo before" role="img" aria-label="Before photo: dated kitchen with oak cabinets and stainless fridge">
      <span class="photo-tag">BEFORE</span>
    </div>
    <div class="compare-photo after" role="img" aria-label="After photo: refaced kitchen with white upper cabinets and stainless appliances">
      <span class="photo-tag">AFTER</span>
    </div>

    <section class="body-copy">
      <p class="lead">We've just completed a kitchen refacing in your area—<br>and the results are stunning. Take a look!</p>
      <ul class="benefit-list">
        <li class="benefit"><svg viewBox="0 0 10 10"><circle cx="5" cy="5" r="5" fill="var(--brand-blue)"/><path d="M2.6 5.2l1.6 1.6 3.2-3.3" stroke="#fff" stroke-width="1.3" fill="none"/></svg>A kitchen refacing takes much less time, and costs up to <span class="highlight">60% less</span> than a full kitchen renovation. Get the kitchen you always dreamed of without all of the disruption of a full renovation.</li>
        <li class="benefit"><svg viewBox="0 0 10 10"><circle cx="5" cy="5" r="5" fill="var(--brand-blue)"/><path d="M2.6 5.2l1.6 1.6 3.2-3.3" stroke="#fff" stroke-width="1.3" fill="none"/></svg>Refacing is a complete kitchen facelift. Replace the doors (and the out-dated style!), trim, and panels and pick something new and fresh. Make any modifications you'd like (is it time to switch that junk cabinet into a pot-and-pan cabinet?).</li>
        <li class="benefit"><svg viewBox="0 0 10 10"><circle cx="5" cy="5" r="5" fill="var(--brand-blue)"/><path d="M2.6 5.2l1.6 1.6 3.2-3.3" stroke="#fff" stroke-width="1.3" fill="none"/></svg>Less mess (no need to empty cupboards), less cost (save up to <span class="highlight">60% of</span> a typical kitchen renovation), save time (a kitchen refacing typically takes only 3 days!)</li>
      </ul>
    </section>

    <address class="contact-panel" style="font-style:normal">
      <div class="contact-item"><svg viewBox="0 0 12 12"><circle cx="6" cy="6" r="6" fill="var(--brand-blue)"/><rect x="4" y="2.5" width="4" height="7" rx=".8" fill="#fff"/></svg>555-014-2290</div>
      <div class="contact-item"><svg viewBox="0 0 12 12"><circle cx="6" cy="6" r="6" fill="var(--brand-blue)"/><rect x="3" y="4" width="6" height="4.2" fill="#fff"/><path d="M3 4l3 2.3L9 4" stroke="var(--brand-blue)" stroke-width=".8" fill="none"/></svg>hello@maplestoneremodels.com</div>
      <div class="contact-item"><svg viewBox="0 0 12 12"><circle cx="6" cy="6" r="6" fill="var(--brand-blue)"/><circle cx="6" cy="6" r="3" stroke="#fff" stroke-width=".8" fill="none"/><path d="M3 6h6M6 3c-1.5 2-1.5 4 0 6M6 3c1.5 2 1.5 4 0 6" stroke="#fff" stroke-width=".6" fill="none"/></svg>www.MaplestoneRemodels.com</div>
      <div class="contact-item"><svg viewBox="0 0 12 12"><circle cx="6" cy="6" r="6" fill="var(--brand-blue)"/><path d="M6 2.3a2.4 2.4 0 0 1 2.4 2.4C8.4 6.5 6 9.6 6 9.6S3.6 6.5 3.6 4.7A2.4 2.4 0 0 1 6 2.3z" fill="#fff"/><circle cx="6" cy="4.7" r=".9" fill="var(--brand-blue)"/></svg>27 Alder Lane, Brookfield,<br>Ontario N0A 1B2</div>
    </address>
  </article>
</body>
</html>
```